Business Card Design For Office Furniture Clearance Company

Kestrel Office Clearance - our company name pretty much explains what we do, we clear offices for high end clients, mainly plc's and large international companies.

We require a nice looking business card that displays professionalism but without being too serious.

It would be nice to see just a little more than a conventional boring business card, make sure you add some flare.

Industry/Entity Type

Office Furniture

Contact Information for Business Card

CARD 1

Mark Holloway
Director
mark@kestrelofficeclear.co.uk
m: 07700 913528

t: 01632 960418
www.kestrelofficeclear.co.uk

Kestrel Office Clearance
Unit K4 B
3-7 Fenwick Lane
Harwick
Dunmere Vale
ZX9 4QT

free office clearances… you cant get better than that.

CARD 2

Peter Donaldson
Director
peter@kestrelofficeclear.co.uk
m: 07700 927153

t: 01632 960418

Kestrel Office Clearance
Unit K4 B
3-7 Fenwick Lane
Harwick
Dunmere Vale
ZX9 4QT

Font styles to use
Sans Serif

Requirements
Must have
• A white background - as we have a blue logo.
Nice to have
• Nice use of the logo - play around with this and dissect it.

```html
<!DOCTYPE html>
<html lang="en">
<head>
<meta charset="utf-8">
<title>Kestrel Office Clearance – Business Card</title>
<link href="https://fonts.googleapis.com/css2?family=Lato:wght@400;700&display=swap" rel="stylesheet">
<style>
  :root {
    --brand-blue: #0a7bc1;
    --brand-blue-dark: #065f99;
    --ink: #2b2b2b;
    --paper: #ffffff;
    --backdrop: #e9e7e4;
  }
  * { margin: 0; padding: 0; box-sizing: border-box; }
  html, body {
    width: 1138px; height: 1200px; overflow: hidden;
    background: var(--backdrop);
    font-family: "Lato", Arial, sans-serif;
  }
  .canvas { position: relative; width: 1138px; height: 1200px; }

  .card {
    position: absolute; left: 218px; width: 671px; height: 384px;
    border-radius: 14px; overflow: hidden;
    box-shadow: 0 3px 8px rgba(0,0,0,0.25);
  }
  .card-front { top: 198px; background: var(--paper); }
  .card-back  { top: 617px; height: 381px; background: var(--brand-blue); }

  .brand-mark {
    position: absolute; left: 490px; top: 38px; width: 108px; height: 108px;
    border-radius: 50%; background: var(--brand-blue);
  }
  .brand-name {
    position: absolute; right: 36px; top: 149px;
    font-weight: 700; font-size: 19px; color: var(--brand-blue); white-space: nowrap;
  }

  .person-name {
    position: absolute; left: 32px; top: 203px;
    font-weight: 700; font-size: 25px; color: var(--brand-blue); white-space: nowrap;
  }
  .person-role {
    position: absolute; left: 32px; top: 232px;
    font-size: 14.5px; line-height: 18px; color: var(--ink);
  }
  .rule {
    position: absolute; left: 93px; top: 243px; width: 547px; height: 1.5px;
    background: var(--ink);
  }

  .contact-list { position: absolute; left: 32px; top: 283px; list-style: none; }
  .contact-list li {
    display: flex; align-items: center; height: 22px;
    font-size: 15.5px; color: var(--ink); letter-spacing: 0.2px; white-space: nowrap;
  }
  .contact-list svg { width: 16px; height: 16px; margin-right: 6px; fill: var(--brand-blue); flex: none; }

  .address {
    position: absolute; left: 446px; top: 290px;
    font-size: 15.5px; line-height: 19.3px; color: var(--ink); font-style: normal; white-space: nowrap;
  }

  .footer-band {
    position: absolute; left: 0; top: 360px; width: 100%; height: 24px;
    background: var(--brand-blue);
  }
  .footer-web {
    position: absolute; right: 0; top: 0; height: 24px; width: 227px;
    background: var(--brand-blue-dark);
    color: #fff; font-size: 13.5px; line-height: 24px; padding-left: 8px; white-space: nowrap;
  }

  .back-mark {
    position: absolute; left: 250px; top: 60px; width: 170px; height: 170px;
    border-radius: 50%; background: var(--brand-blue-dark);
  }
  .back-name {
    position: absolute; left: 0; width: 100%; top: 252px; text-align: center;
    color: #fff; font-weight: 700; font-size: 30px; white-space: nowrap;
  }
  .back-web {
    position: absolute; left: 0; width: 100%; top: 342px; text-align: center;
    color: #fff; font-size: 15.5px; white-space: nowrap;
  }
</style>
</head>
<body>
<div class="canvas">

  <section class="card card-front">
    <div class="brand-mark"></div>
    <div class="brand-name">Kestrel Office Clearance</div>

    <div class="person-name">Mark Holloway</div>
    <div class="person-role">Director</div>
    <div class="rule"></div>

    <ul class="contact-list">
      <li>
        <svg viewBox="0 0 16 16" aria-hidden="true"><path d="M4 1h8a1 1 0 0 1 1 1v12a1 1 0 0 1-1 1H4a1 1 0 0 1-1-1V2a1 1 0 0 1 1-1zm.8 1.6v9.6h6.4V2.6zM8 12.8a.8.8 0 1 0 0 1.6.8.8 0 0 0 0-1.6z"/></svg>
        07700 913528
      </li>
      <li>
        <svg viewBox="0 0 16 16" aria-hidden="true"><path d="M3.6 1.2l2.3 2.6-1.2 1.8c.9 2.2 2.6 3.9 4.8 4.8l1.8-1.2 2.6 2.3-1.6 2.6C7 13.6 2.4 9 1.1 3z"/></svg>
        01632 960418
      </li>
      <li>
        <svg viewBox="0 0 16 16" aria-hidden="true"><path d="M1 3.5h14v9H1zm1.4 1.2L8 9l5.6-4.3zM2.2 11.5h11.6L9.9 7.9 8 9.3 6.1 7.9z"/></svg>
        mark@kestrelofficeclear.co.uk
      </li>
    </ul>

    <address class="address">
      Unit K4 B, 3-7 Fenwick Lane<br>
      Harwick, Dunmere Vale<br>
      ZX9 4QT
    </address>

    <div class="footer-band">
      <div class="footer-web">www.kestrelofficeclear.co.uk</div>
    </div>
  </section>

  <section class="card card-back">
    <div class="back-mark"></div>
    <div class="back-name">Kestrel Office Clearance</div>
    <div class="back-web">www.kestrelofficeclear.co.uk</div>
  </section>

</div>
</body>
</html>
```